Zielgruppe
Unsere Firma produziert individuelles Büromaterialen aus Papier & Kunststoff (bspw. Ringbücher, Klarsichthüllen, Mappen, etc.) Zielgruppe sind (eher konservative) Unternehmenskunden in allen Branchen (speziell Logistik, KFZ, Gesundheit).
Die Broschüre soll primär zur Neukundenakquise als auch für Neuverkäufe an Bestandskunden verwendet werden und in einem schlichten, modernen und hochwertigen Design eine Übersicht über unser Produktportfolio bieten.
Aufgabenstellung
Die Broschüre soll auf Basis des bestehenden Corporate Designs gestaltet werden.
1) In der Broschüre soll jede unserer fünf Produktkategorien (Ordner, Ringbuchordner, Ordnerregister, Hüllen & Taschen, Mappen) eine eigene Seite/Abschnitt erhalten, ähnlich unserer Website.
2) Zudem soll auf einer eigenen Seite/Abschnitt prägnant darauf hingewiesen werden, dass wir für alle Produktkategorie individuelle Sonderanfertigungen anbieten.
Die Strukturierung und Aufteilung der Inhalt in der Broschüre soll sich relativ klar an unserer Website orientieren. Medien & bereits vorhandene Texte sind sowohl als Anlage dem Projekt beigefügt, als auch auf unserer Website auffindbar. Falls notwendig wären wir auch bereit zu einzelnen Themenbereiche neue Texte erstellen zu lassen.
Hinsichtlich des Formats überlassen wir die Auswahl dem Designer. Die Broschüre wird jedoch auch häufig in digitaler Form versandt.

```html
<!DOCTYPE html>
<html lang="de">
<head>
<meta charset="utf-8">
<title>Falkner Büroform – Produktübersicht 2022</title>
<link href="https://fonts.googleapis.com/css2?family=Exo+2:wght@400;500&display=swap" rel="stylesheet">
<style>
  :root {
    --navy: #173f8a;
    --navy-soft: #2f5aa3;
    --mist: #d3d9e6;
    --periwinkle: #a3aed6;
    --paper: #f7f7f8;
    --ink: #3a3f4a;
    --stage: #a7afb7;
    --photo-top: #5d636b;
    --photo-mid: #9aa6b3;
    --photo-low: #dfe6ef;
  }
  * { margin: 0; padding: 0; box-sizing: border-box; }
  html, body { width: 1200px; height: 960px; overflow: hidden; }
  body {
    background: var(--stage);
    font-family: "Exo 2", sans-serif;
    color: var(--ink);
    position: relative;
  }
  .spread {
    position: absolute;
    left: 20px; top: 70px;
    width: 1160px; height: 820px;
    display: flex;
    box-shadow: 0 10px 30px rgba(40,50,60,.25);
  }
  .page {
    position: relative;
    width: 580px; height: 820px;
    background: var(--paper);
    overflow: hidden;
  }
  /* back cover */
  .back-band {
    position: absolute; left: 0; right: 0;
    top: 520px; height: 200px;
    background: var(--mist);
  }
  .back-brand {
    position: absolute; left: 56px; top: 556px;
  }
  .brand-name {
    display: flex; align-items: center; gap: 8px;
    font-size: 17px; font-weight: 400; color: var(--ink);
    letter-spacing: .5px;
  }
  .brand-square {
    width: 14px; height: 14px;
    border: 2px solid var(--navy);
  }
  .brand-tagline {
    font-size: 8px; color: var(--navy-soft);
    letter-spacing: .6px; margin-top: 2px;
  }
  .contact { margin-top: 26px; font-size: 10px; line-height: 1.45; color: var(--ink); }
  .contact .firm { color: var(--navy); font-size: 11px; }
  /* front cover */
  .front-brand {
    position: absolute; right: 26px; top: 40px; text-align: right;
  }
  .front-brand .brand-name { justify-content: flex-end; }
  .cover-photo {
    position: absolute; left: 0; top: 120px;
    width: 560px; height: 500px;
    background: linear-gradient(180deg, var(--photo-top) 0%, var(--photo-mid) 45%, var(--photo-low) 80%, #c9d0d8 100%);
  }
  .headline-veil {
    position: absolute; left: 0; top: 420px;
    width: 560px; height: 200px;
    background: rgba(222,228,240,.75);
  }
  .edge-bar { position: absolute; right: 0; width: 20px; }
  .edge-bar.top { top: 120px; height: 300px; background: var(--navy); }
  .edge-bar.mid { top: 420px; height: 130px; background: var(--periwinkle); }
  .edge-bar.low { top: 550px; height: 70px; background: var(--navy); }
  .headline {
    position: absolute; left: 150px; top: 460px;
    font-size: 27px; font-weight: 500; line-height: 1.25;
    color: var(--navy); letter-spacing: 1px;
  }
  .edition {
    position: absolute; left: 150px; top: 548px;
    font-size: 12px; letter-spacing: 1.2px; color: var(--ink);
  }
</style>
</head>
<body>
  <div class="spread">
    <section class="page back-cover">
      <div class="back-band"></div>
      <div class="back-brand">
        <div class="brand-name"><span class="brand-square"></span>Falkner Büroform</div>
        <div class="brand-tagline">Qualität für jedes Büro.</div>
        <div class="contact">
          <div class="firm">Falkner UG Papier-<br>&amp; Kunststoffverarbeitung</div>
          <div>Lindenstieg 12</div>
          <div>45127 Wendhausen</div>
          <div>Telefon: +49 2100 5566 30</div>
          <div>E-Mail: kontakt@falkner-bueroform.de</div>
        </div>
      </div>
    </section>
    <section class="page front-cover">
      <div class="front-brand">
        <div class="brand-name"><span class="brand-square"></span>Falkner Büroform</div>
        <div class="brand-tagline">Qualität für jedes Büro.</div>
      </div>
      <div class="cover-photo" role="img" aria-label="Fotografie einer Produktionsmaschine für Papier- und Kunststoffverarbeitung"></div>
      <div class="headline-veil"></div>
      <div class="edge-bar top"></div>
      <div class="edge-bar mid"></div>
      <div class="edge-bar low"></div>
      <h1 class="headline">Papier und Kunststoff<br>sind unser Ding!</h1>
      <p class="edition">PRODUKTÜBERSICHT 2022</p>
    </section>
  </div>
</body>
</html>
```